Vexor Ridge website

i'm looking for a promotional website for my business.
we provide Rope Access, Work at Height & Difficult Access services.
we treat water leak into buildings, external renovation of buildings, windows cleaning, confined spaces services and practically jobs in which the access is difficult.
here are examples of web site i like :
http://www.pixelbarnwebs.example/site-themes/51827.html
http://www.pixelbarnwebs.example/page-templates/62914.html

Target Market(s)

private people, commercial household chiefs, maintenance managers

Industry/Entity Type

Business

Requirements
Must have
• - mobile friendly
- chatterbay redirection
- 5 tabs
- one more customizable page - so i can add a photo and a description of the service corresponding (for now i offer 7 different services)
- contact us on each page with no redirection
- we are offering 7 different services
the website will be published in Israel which means right to left or centered for english option in the future. (logo on left hand corner)

- no flash
- should be future customisable - for future
Nice to have
• - a space for a slogan
- non scrollable
- photos on the landing page + redirection to gallery (photos and short films)
- 3 dynamic banners with short description of the theme of each, clicking on the banner after it opened will redirect to it's corresponding page.

```html
<!DOCTYPE html>
<html lang="en">
<head>
<meta charset="utf-8">
<title>Vexor Ridge — Projects</title>
<link href="https://fonts.googleapis.com/css2?family=Montserrat:wght@400;500&family=Oswald:wght@600&display=swap" rel="stylesheet">
<style>
  :root {
    --header-bg: #363636;
    --page-bg: #2b2b2b;
    --footer-bg: #1e1e1e;
    --nav-active: #0b0b0b;
    --text-light: #ffffff;
    --text-muted: #a9a9a9;
    --text-footer: #b5b5b5;
    --rule: #555555;
    --frame: #050505;
    --logo-disc: #ffffff;
    --social-a: #3b5a98;
    --social-b: #3fa9df;
    --social-c: #1f7bb6;
  }
  * { margin: 0; padding: 0; box-sizing: border-box; }
  html, body { width: 1200px; height: 1012px; overflow: hidden; }
  body {
    position: relative;
    background: var(--page-bg);
    font-family: "Montserrat", Arial, sans-serif;
    color: var(--text-light);
  }
  .site-header {
    position: absolute; left: 0; top: 0; width: 1200px; height: 80px;
    background: var(--header-bg);
  }
  .hero {
    position: absolute; left: 0; top: 0; width: 1200px; height: 560px;
  }
  .brand-disc {
    position: absolute; left: 138px; top: -78px; width: 192px; height: 192px;
    border-radius: 50%; background: var(--logo-disc);
  }
  .brand-name {
    position: absolute; left: 342px; top: 17px;
    font-family: "Oswald", "Arial Narrow", sans-serif; font-weight: 600;
    font-size: 27px; letter-spacing: 0.2px; color: var(--text-light);
    text-transform: uppercase;
  }
  .main-nav {
    position: absolute; top: 0; right: 134px; display: flex; height: 79px;
  }
  .main-nav a {
    display: block; height: 79px; line-height: 72px; padding: 0 12px;
    color: var(--text-light); text-decoration: none;
    font-size: 17px; font-weight: 500; letter-spacing: 0.4px;
  }
  .main-nav a.is-active { background: var(--nav-active); }
  .projects {
    position: absolute; left: 150px; top: 548px; width: 904px;
  }
  .projects-title {
    font-size: 24px; font-weight: 500; padding-bottom: 10px;
    border-bottom: 1px dotted var(--rule);
  }
  .project-list { display: flex; justify-content: space-between; margin-top: 22px; }
  .project { width: 282px; }
  .project-thumb {
    display: block; width: 282px; height: 157px;
    border: 5px solid var(--frame);
    background: linear-gradient(100deg, #c9ccd0 0%, #9aa3ad 30%, #2e3c52 55%, #c2c3bd 80%, #8d8e86 100%);
  }
  .project-name { font-size: 14px; font-weight: 500; margin-top: 16px; }
  .project-text {
    font-size: 13.6px; line-height: 19.2px; color: var(--text-muted); margin-top: 8px;
  }
  .site-footer {
    position: absolute; left: 0; top: 0; width: 1200px; height: 1012px; pointer-events: none;
  }
  .footer-legal {
    position: absolute; left: 151px; top: 976px;
    font-size: 13px; color: var(--text-footer); letter-spacing: 0.3px;
  }
  .footer-social {
    position: absolute; right: 148px; top: 969px; display: flex; align-items: center;
  }
  .footer-social-label { font-size: 13px; color: var(--text-light); margin-right: 10px; letter-spacing: 0.3px; }
  .social-square { width: 29px; height: 29px; border-radius: 3px; margin-left: 6px; }
  .social-square.is-a { background: var(--social-a); }
  .social-square.is-b { background: var(--social-b); }
  .social-square.is-c { background: var(--social-c); }
</style>
</head>
<body>
  <header class="site-header"></header>

  <svg class="hero" viewBox="0 0 1200 560" role="img" aria-label="Photo of two rope access technicians cleaning the glass facade of an office building">
    <defs>
      <linearGradient id="heroTone" x1="0" y1="0" x2="1" y2="1">
        <stop offset="0" stop-color="#7d8590"/>
        <stop offset="0.35" stop-color="#3f4c5c"/>
        <stop offset="0.7" stop-color="#26313f"/>
        <stop offset="1" stop-color="#4b5058"/>
      </linearGradient>
    </defs>
    <polygon points="0,66 1200,82 1200,486 0,542" fill="url(#heroTone)"/>
  </svg>

  <div class="brand-disc" aria-hidden="true"></div>
  <div class="brand-name">Vexor Ridge</div>

  <nav class="main-nav">
    <a href="#">HOME</a>
    <a href="#">SERVICES</a>
    <a href="#" class="is-active">PROJECTS</a>
    <a href="#">GALLERY</a>
    <a href="#">CONTACT US</a>
  </nav>

  <section class="projects">
    <h2 class="projects-title">Projects</h2>
    <div class="project-list">
      <article class="project">
        <span class="project-thumb" role="img" aria-label="Photo of a technician abseiling beside building windows"></span>
        <h3 class="project-name">Project Name</h3>
        <p class="project-text">Lorem ipsum dolor sit amet, consectetur adipisicing elit, sed do eiusmod tempor incididunt ut labore et dolore magna aliqua. Ut enim ad minim veniam</p>
      </article>
      <article class="project">
        <span class="project-thumb" role="img" aria-label="Photo of a technician abseiling beside building windows"></span>
        <h3 class="project-name">Project Name</h3>
        <p class="project-text">Lorem ipsum dolor sit amet, consectetur adipisicing elit, sed do eiusmod tempor incididunt ut labore et dolore magna aliqua. Ut enim ad minim veniam</p>
      </article>
      <article class="project">
        <span class="project-thumb" role="img" aria-label="Photo of a technician abseiling beside building windows"></span>
        <h3 class="project-name">Project Name</h3>
        <p class="project-text">Lorem ipsum dolor sit amet, consectetur adipisicing elit, sed do eiusmod tempor incididunt ut labore et dolore magna aliqua. Ut enim ad minim veniam</p>
      </article>
    </div>
  </section>

  <footer>
    <svg class="site-footer" viewBox="0 0 1200 1012" aria-hidden="true">
      <polygon points="0,924 1200,960 1200,1012 0,1012" fill="var(--footer-bg)"/>
    </svg>
    <p class="footer-legal">VEXOR RIDGE © 2013 &nbsp;|&nbsp; PRIVACY POLICY</p>
    <div class="footer-social">
      <span class="footer-social-label">CONNECT WITH US</span>
      <span class="social-square is-a" aria-label="chatterbay"></span>
      <span class="social-square is-b" aria-label="Chirpline"></span>
      <span class="social-square is-c" aria-label="Linkwork"></span>
    </div>
  </footer>
</body>
</html>
```